Financial Service Company Need Business Card Design

This is a new startup company, first of its kind to offer this service. We facilitate the movement of deposit funds electronically between home buyers and real estate brokerages.Our customers are DOMIVANS®, real estate brokerages, and home buyers, we identify ourselves as a financial/technology company.
Not looking for anything too flashy. Just a clean design that shows the logo, contact info, etc. Company colors can be seen on attached logo, and 'coming soon page'
www.quorvanta.ca

```html
<!DOCTYPE html>
<html lang="en">
<head>
<meta charset="utf-8">
<title>Quorvanta Business Card</title>
<link href="https://fonts.googleapis.com/css2?family=Mulish:wght@400;600;700&display=swap" rel="stylesheet">
<style>
  :root {
    --page-bg: #e9e9e9;
    --card-white: #ffffff;
    --card-grey: #7a797b;
    --brand-orange: #ee6f2d;
    --text-grey: #8a898b;
    --name-grey: #7d7c7e;
    --light-text: #f7f5f2;
  }
  * { box-sizing: border-box; margin: 0; padding: 0; }
  html, body {
    width: 1200px;
    height: 1000px;
    overflow: hidden;
  }
  body {
    background: var(--page-bg);
    font-family: "Mulish", sans-serif;
    display: flex;
    flex-direction: column;
    align-items: center;
    justify-content: center;
    gap: 60px;
  }
  .card {
    width: 700px;
    height: 400px;
    position: relative;
    box-shadow: 0 6px 18px rgba(0,0,0,0.18);
  }
  .card--front {
    background: var(--card-white);
    display: flex;
  }
  .card--back {
    background: var(--card-grey);
    display: flex;
    align-items: center;
    justify-content: center;
  }
  .brand {
    display: flex;
    align-items: center;
    gap: 12px;
  }
  .brand__square {
    width: 30px;
    height: 30px;
    background: var(--brand-orange);
  }
  .brand__name {
    font-weight: 700;
    letter-spacing: -0.5px;
  }
  .card--front .brand__name {
    color: var(--text-grey);
    font-size: 36px;
  }
  .card--back .brand__square {
    width: 46px;
    height: 46px;
  }
  .card--back .brand__name {
    color: var(--light-text);
    font-size: 58px;
  }
  .front__logo-side {
    width: 360px;
    display: flex;
    align-items: center;
    justify-content: center;
    padding-top: 40px;
  }
  .front__divider {
    width: 3px;
    height: 240px;
    background: var(--brand-orange);
    margin-top: 40px;
  }
  .front__contact {
    padding: 38px 0 0 50px;
    color: var(--text-grey);
    font-size: 19px;
  }
  .contact__name {
    font-size: 25px;
    font-weight: 600;
    color: var(--name-grey);
  }
  .contact__title {
    font-size: 18px;
    margin-top: 6px;
  }
  .contact__address { margin-top: 40px; }
  .contact__phone { margin-top: 20px; }
  .contact__email { margin-top: 20px; }
  .contact__web { margin-top: 4px; }
</style>
</head>
<body>
  <section class="card card--front">
    <div class="front__logo-side">
      <div class="brand">
        <span class="brand__square"></span>
        <span class="brand__name">Quorvanta</span>
      </div>
    </div>
    <div class="front__divider"></div>
    <div class="front__contact">
      <p class="contact__name">Name Last</p>
      <p class="contact__title">Title</p>
      <p class="contact__address">Address 123 - City</p>
      <p class="contact__phone">123 456 789</p>
      <p class="contact__email">hello@quorvanta.ca</p>
      <p class="contact__web">www.quorvanta.ca</p>
    </div>
  </section>

  <section class="card card--back">
    <div class="brand">
      <span class="brand__square"></span>
      <span class="brand__name">Quorvanta</span>
    </div>
  </section>
</body>
</html>
```